Kellow Family Law, legal technician needs a website and design

I need a website for a family law practice. I specialize in collaborative law, unbundled services, and mediation. The website must contain my company logo (file attached), and the website must be a mixture of my personality and my profession. I have attached additional information to explain my personality and profession.

Target Market(s)

Lower through middle-class (income level up to $200,000 per year)

Coding

Coded - Design and coding required

Number of Pages Required

1 page

Requirements
Must have
• Must have enough pages to cover required content. I submitted below some content about the collaborative law process. All of the content is not necessary. However, the website must have enough content to clearly describe the services I offer. Use your professionalism and judgment regarding font, font size, etc.

```html
<!DOCTYPE html>
<html lang="en">
<head>
<meta charset="utf-8">
<title>Kellow Family Law</title>
<link href="https://fonts.googleapis.com/css2?family=Playfair+Display:wght@600;700;800&family=Poppins:wght@400;500;600&display=swap" rel="stylesheet">
<style>
:root{
  --olive:#aaa53a;
  --olive-dark:#8f8a2a;
  --olive-light:#d5d17e;
  --navy:#0c1738;
  --navy-2:#14224b;
  --ink:#1c1c24;
  --muted:#77777f;
  --line:#e3e3e8;
  --white:#ffffff;
  --soft:#f4f4f6;
}
*{box-sizing:border-box;margin:0;padding:0}
html,body{width:1200px;height:4816px;overflow:hidden}
body{position:relative;background:var(--white);font-family:"Poppins",Arial,sans-serif;color:var(--ink);font-size:13px}
.serif{font-family:"Playfair Display",Georgia,serif}
.abs{position:absolute}
.btn{display:inline-block;background:var(--olive);color:var(--white);font-size:12px;font-weight:600;letter-spacing:.5px;padding:12px 24px;text-transform:uppercase}
.btn-outline{display:inline-block;border:1px solid var(--ink);font-size:11px;font-weight:600;padding:10px 20px;text-transform:uppercase}
.section-title{position:absolute;left:0;width:1200px;text-align:center;font-family:"Playfair Display",Georgia,serif;font-weight:700;font-size:34px;color:var(--navy);text-transform:uppercase}
.photo{position:absolute}

/* header */
.site-header{position:absolute;left:0;top:0;width:1200px;height:120px;background:var(--white)}
.brand{position:absolute;left:60px;top:14px;display:flex;align-items:center;gap:12px}
.brand-mark{width:56px;height:56px;background:var(--olive)}
.brand-name{font-family:"Playfair Display",Georgia,serif;font-weight:700;font-size:22px;line-height:1.05;color:var(--olive);text-transform:uppercase}
.topbar{position:absolute;left:460px;top:0;width:680px;height:32px;background:var(--navy);color:var(--white);font-size:11px;display:flex;align-items:center;gap:40px;padding-left:24px}
.topbar span{display:flex;align-items:center;gap:8px}
.main-nav{position:absolute;left:360px;top:62px;display:flex;gap:34px;font-size:13px;font-weight:500;color:var(--ink)}
.nav-cta{position:absolute;right:60px;top:54px;border:1px solid var(--ink);padding:8px 16px;font-size:11px;font-weight:600}

/* hero */
.hero{position:absolute;left:0;top:120px;width:1200px;height:700px;background:linear-gradient(100deg,#3d3b38 0%,#6d6a66 35%,#b8b4ae 70%,#d9d5cf 100%)}
.hero-title{position:absolute;left:90px;top:200px;color:var(--white);font-family:"Playfair Display",Georgia,serif}
.hero-title .big{font-size:96px;font-weight:800;line-height:1}
.hero-title .sub{font-size:46px;font-weight:600;line-height:1.1;letter-spacing:1px}
.hero-lead{position:absolute;left:90px;top:372px;width:380px;color:var(--white);font-size:15px;line-height:1.5}
.hero .btn{position:absolute;left:90px;top:440px}
.dots{position:absolute;left:180px;top:820px}

/* services */
.service-card{position:absolute;top:968px;width:290px;height:290px;background:var(--white);box-shadow:0 8px 30px rgba(12,23,56,.12);text-align:center;padding:46px 30px 0}
.service-card h3{font-family:"Playfair Display",Georgia,serif;font-size:15px;font-weight:700;color:var(--navy);margin:22px 0 14px;text-transform:uppercase}
.service-card p{font-size:12px;line-height:1.7;color:var(--muted)}

/* experience */
.exp-text{position:absolute;left:612px;top:1510px;width:520px}
.exp-text h2{font-family:"Playfair Display",Georgia,serif;font-size:34px;line-height:1.15;font-weight:700;color:var(--navy);text-transform:uppercase}
.exp-text p{font-size:12px;color:var(--muted);margin-top:10px}
.stats{position:absolute;left:612px;top:1680px;display:flex;gap:44px}
.stat b{display:block;font-family:"Playfair Display",Georgia,serif;font-size:36px;color:var(--navy)}
.stat b i{font-style:normal;color:var(--olive)}
.stat span{font-size:10px;font-weight:600;color:var(--muted);text-transform:uppercase}

/* about */
.about-text{position:absolute;left:90px;top:2036px;width:470px}
.eyebrow{display:flex;align-items:center;gap:16px;font-size:12px;font-weight:600;text-transform:uppercase}
.eyebrow:before{content:"";width:60px;height:2px;background:var(--ink)}
.about-text h2{font-family:"Playfair Display",Georgia,serif;font-size:38px;line-height:1.12;font-weight:700;color:var(--navy);margin:18px 0 20px;text-transform:uppercase}
.about-text p{font-size:13px;line-height:1.7;color:var(--muted);margin-bottom:28px}
.play{position:absolute;left:622px;top:2180px}

/* blog */
.blog{position:absolute;left:0;top:2500px;width:1200px;height:700px;background:linear-gradient(90deg,var(--olive-dark) 0%,var(--olive) 55%,#c9c57a 100%)}
.blog-ghost{position:absolute;right:0;top:-14px;font-family:"Playfair Display",Georgia,serif;font-weight:800;font-size:120px;color:rgba(255,255,255,.18);text-transform:uppercase}
.blog .section-title{top:140px;color:var(--white)}
.post{position:absolute;top:200px;width:306px;height:400px;background:var(--white)}
.post .photo{left:0;top:0;width:306px;height:210px}
.post .body{position:absolute;left:24px;top:230px;width:260px}
.post .date{display:inline-block;background:var(--soft);font-size:10px;padding:4px 10px;color:var(--muted)}
.post h4{font-family:"Playfair Display",Georgia,serif;font-size:15px;font-weight:700;color:var(--navy);margin:14px 0 8px;text-transform:uppercase}
.post p{font-size:11px;color:var(--muted);line-height:1.6}
.post .more{display:inline-block;margin-top:10px;font-size:10px;font-weight:600;color:var(--olive);text-transform:uppercase}

/* contact */
.contact .section-title{top:3280px}
.info-item{position:absolute;left:210px;display:flex;gap:20px;width:260px}
.info-icon{width:50px;height:50px;background:var(--navy);display:flex;align-items:center;justify-content:center;flex:none}
.info-item b{display:block;font-size:12px;font-weight:600;text-transform:uppercase}
.info-item span{font-size:11px;color:var(--muted);line-height:1.5}
.field{position:absolute}
.field label{display:block;font-size:10px;font-weight:600;text-transform:uppercase;margin-bottom:6px}
.field div{background:var(--soft);border:1px solid var(--line);height:36px;font-size:11px;color:#a0a0a8;padding:10px 12px}
.send{position:absolute;left:520px;top:3636px;background:var(--olive);color:var(--white);font-weight:600;font-size:14px;padding:10px 32px;text-transform:uppercase}

/* banner */
.banner{position:absolute;left:0;top:3800px;width:1200px;height:432px;background:linear-gradient(90deg,#f0efec,#ffffff)}
.banner-text{position:absolute;left:646px;top:80px;width:470px}
.banner-text h2{font-family:"Playfair Display",Georgia,serif;font-size:44px;line-height:1.05;font-weight:700;color:var(--navy);text-transform:uppercase}
.banner-text p{font-size:15px;line-height:1.5;color:var(--ink);margin:16px 0 26px}

/* footer */
.site-footer{position:absolute;left:0;top:4232px;width:1200px;height:584px;background:var(--navy);color:var(--white)}
.site-footer .section-title{top:88px;color:var(--white);font-size:34px}
.newsletter{position:absolute;left:330px;top:144px;width:540px;height:48px;background:var(--white);display:flex;align-items:center;padding-left:18px;font-size:12px;color:#8a8a92}
.newsletter .go{position:absolute;right:0;top:0;width:56px;height:48px;background:var(--olive)}
.foot-brand{position:absolute;left:96px;top:270px;display:flex;align-items:center;gap:12px}
.socials{position:absolute;left:150px;top:370px;display:flex;gap:12px}
.socials span{width:26px;height:26px;border-radius:50%;background:var(--navy-2);border:1px solid #2c3a66}
.foot-col{position:absolute;top:270px;font-size:12px;line-height:2}
.foot-col h5{font-size:14px;font-weight:600;text-transform:uppercase;margin-bottom:8px}
.foot-col a{display:block;color:#c4c8d6;text-decoration:none}
.copyright{position:absolute;left:0;top:530px;width:1200px;text-align:center;font-size:11px;color:#c4c8d6;border-top:1px solid #223061;padding-top:18px;text-transform:uppercase}
</style>
</head>
<body>

<header class="site-header">
  <div class="brand"><div class="brand-mark"></div><div class="brand-name">Kellow<br>Family Law</div></div>
  <div class="topbar">
    <span><svg width="12" height="12" viewBox="0 0 24 24"><path fill="#fff" d="M6.6 10.8a15 15 0 006.6 6.6l2.2-2.2c.3-.3.7-.4 1-.2 1.1.4 2.3.6 3.6.6.6 0 1 .4 1 1V20c0 .6-.4 1-1 1A17 17 0 013 4c0-.6.4-1 1-1h3.5c.6 0 1 .4 1 1 0 1.3.2 2.5.6 3.6.1.3 0 .7-.2 1z"/></svg>Call us : +00 321 654 0987</span>
    <span><svg width="12" height="12" viewBox="0 0 24 24"><path fill="#fff" d="M12 2a7 7 0 00-7 7c0 5 7 13 7 13s7-8 7-13a7 7 0 00-7-7zm0 9.5A2.5 2.5 0 1112 6a2.5 2.5 0 010 5.5z"/></svg>Some address line goes here city name</span>
  </div>
  <nav class="main-nav"><span>Collaborative Law</span><span>Cost &amp; Fees</span><span>Mediation</span><span>Trusting In The Collaborative</span><span>Blog &amp; Articles</span></nav>
  <div class="nav-cta">CONTACT ME</div>
</header>

<section class="hero">
  <div class="photo" role="img" aria-label="Photo of two lawyers reviewing a document together in an office" style="left:0;top:0;width:1200px;height:700px"></div>
  <div class="hero-title"><div class="big">KELLOW</div><div class="sub">FAMILY LAW</div></div>
  <p class="hero-lead">Collaborative law and unbundled legal services in King County, Washington state.</p>
  <span class="btn">Contact Me</span>
</section>

<svg class="dots" width="120" height="40" viewBox="0 0 120 40">
  <g fill="#aaa53a"><circle cx="6" cy="6" r="5"/><circle cx="38" cy="6" r="5"/><circle cx="70" cy="6" r="5"/><circle cx="102" cy="6" r="5"/><circle cx="6" cy="32" r="5"/><circle cx="38" cy="32" r="5"/><circle cx="70" cy="32" r="5"/><circle cx="102" cy="32" r="5"/></g>
</svg>

<section class="services">
  <h2 class="section-title" style="top:900px">I Specialize In Kellow</h2>
  <div class="service-card" style="left:160px">
    <svg width="64" height="54" viewBox="0 0 64 54" fill="none" stroke="#0c1738" stroke-width="2"><path d="M4 20l12-10 10 6 8-4 10 6 16-8"/><path d="M16 10l16 20c2 3 6 1 4-2l-8-10"/><path d="M22 32l6 6M28 28l8 8"/><circle cx="32" cy="44" r="4"/></svg>
    <h3>Collaborative Law</h3>
    <p>It is a long established fact that a reader will be distracted by the readable content</p>
  </div>
  <div class="service-card" style="left:455px">
    <svg width="64" height="54" viewBox="0 0 64 54" fill="none" stroke="#0c1738" stroke-width="2"><path d="M32 4v44M16 48h32M8 12h48"/><path d="M14 12L6 30h16zM50 12l-8 18h16z"/><path d="M6 30a8 5 0 0016 0M42 30a8 5 0 0016 0"/></svg>
    <h3>Unbundled Services</h3>
    <p>It is a long established fact that a reader will be distracted by the readable content</p>
  </div>
  <div class="service-card" style="left:750px">
    <svg width="64" height="54" viewBox="0 0 64 54" fill="none" stroke="#0c1738" stroke-width="2"><circle cx="14" cy="16" r="6"/><circle cx="50" cy="16" r="6"/><circle cx="32" cy="12" r="6"/><path d="M4 40c0-8 4-14 10-14s10 6 10 14M40 40c0-8 4-14 10-14s10 6 10 14M22 36c0-8 4-14 10-14s10 6 10 14"/><path d="M2 48h60"/></svg>
    <h3>Our Mediation</h3>
    <p>It is a long established fact that a reader will be distracted by the readable content</p>
  </div>
</section>

<section class="experience">
  <div class="photo" role="img" aria-label="Photo of a legal team discussing papers around a laptop" style="left:0;top:1408px;width:640px;height:452px;background:linear-gradient(120deg,#8a8884,#cfcbc4 60%,#e9e6e1)"></div>
  <div class="exp-text">
    <h2>50 Years Of Experience In Various Cases</h2>
    <p>Aenean tristique ex leo, at efficitur libero rhoncus sed, bibendum et.</p>
  </div>
  <div class="stats">
    <div class="stat"><b>90<i>+</i></b><span>Awards</span></div>
    <div class="stat"><b>3K<i>+</i></b><span>Cases Won</span></div>
    <div class="stat"><b>2K<i>+</i></b><span>Clients</span></div>
    <div class="stat"><b>200<i>+</i></b><span>Attorneys</span></div>
  </div>
</section>

<section class="about">
  <div class="about-text">
    <div class="eyebrow">About Us</div>
    <h2>About Kellow Family Law A Legal Technician</h2>
    <p>Aenean sollicitudin lorem quis bibendum auctor nisi elit consequat ipsum nec sagittis sem nibh id elit. Duis sed odio sit amet nibh vulputate cursus a sit amet mauris. Morbi accumsan ipsum velit.</p>
    <span class="btn-outline">Learn More</span>
  </div>
  <div class="photo" role="img" aria-label="Photo of a lawyer in a suit reading a document at a desk" style="left:672px;top:1920px;width:440px;height:520px;background:linear-gradient(160deg,#6e6c69,#b3afa9 55%,#e4e0da)"></div>
  <svg class="play" width="100" height="100" viewBox="0 0 100 100"><circle cx="50" cy="50" r="50" fill="#aaa53a"/><path d="M42 34l24 16-24 16z" fill="#fff"/></svg>
</section>

<section class="blog">
  <div class="blog-ghost">Kellow</div>
  <h2 class="section-title">Blog And Articles</h2>
  <article class="post" style="left:132px">
    <div class="photo" role="img" aria-label="Photo of a couple meeting with a lawyer" style="background:linear-gradient(135deg,#5d5a56,#b9b4ad)"></div>
    <div class="body"><span class="date">20-05-2022</span><h4>Blog Heading Goes Here</h4><p>Aenean sollicitudin lorem nec sagittis sem nibh id elit duis sed odio.</p><span class="more">Read More</span></div>
  </article>
  <article class="post" style="left:447px">
    <div class="photo" role="img" aria-label="Photo of lawyers in a meeting room" style="background:linear-gradient(135deg,#7a7773,#d6d2cb)"></div>
    <div class="body"><span class="date">20-05-2022</span><h4>Blog Heading Goes Here</h4><p>Aenean sollicitudin lorem nec sagittis sem nibh id elit duis sed odio.</p><span class="more">Read More</span></div>
  </article>
  <article class="post" style="left:762px">
    <div class="photo" role="img" aria-label="Photo of hands signing a contract on a desk" style="background:linear-gradient(135deg,#6b5a48,#c9b9a4)"></div>
    <div class="body"><span class="date">20-05-2022</span><h4>Blog Heading Goes Here</h4><p>Aenean sollicitudin lorem nec sagittis sem nibh id elit duis sed odio.</p><span class="more">Read More</span></div>
  </article>
</section>

<section class="contact">
  <h2 class="section-title">Contact Me</h2>
  <div class="info-item" style="top:3360px">
    <div class="info-icon"><svg width="20" height="20" viewBox="0 0 24 24"><path fill="#fff" d="M12 2a7 7 0 00-7 7c0 5 7 13 7 13s7-8 7-13a7 7 0 00-7-7zm0 9.5A2.5 2.5 0 1112 6a2.5 2.5 0 010 5.5z"/></svg></div>
    <div><b>Location*</b><span>Some address line goes here city name</span></div>
  </div>
  <div class="info-item" style="top:3450px">
    <div class="info-icon"><svg width="20" height="20" viewBox="0 0 24 24"><path fill="#fff" d="M6.6 10.8a15 15 0 006.6 6.6l2.2-2.2c.3-.3.7-.4 1-.2 1.1.4 2.3.6 3.6.6.6 0 1 .4 1 1V20c0 .6-.4 1-1 1A17 17 0 013 4c0-.6.4-1 1-1h3.5c.6 0 1 .4 1 1 0 1.3.2 2.5.6 3.6.1.3 0 .7-.2 1z"/></svg></div>
    <div><b>Call*</b><span>+00 321 654 0987</span></div>
  </div>
  <div class="info-item" style="top:3540px">
    <div class="info-icon"><svg width="20" height="20" viewBox="0 0 24 24"><path fill="#fff" d="M3 5h18v14H3z"/><path d="M3 5l9 7 9-7" stroke="#0c1738" stroke-width="2" fill="none"/></svg></div>
    <div><b>Email Us*</b><span>hello@kellowlaw.test</span></div>
  </div>
  <div class="field" style="left:520px;top:3350px;width:220px"><label>Name*</label><div>Enter your name</div></div>
  <div class="field" style="left:770px;top:3350px;width:220px"><label>Email*</label><div>Enter your email</div></div>
  <div class="field" style="left:520px;top:3420px;width:220px"><label>Phone*</label><div>Enter your phone</div></div>
  <div class="field" style="left:770px;top:3420px;width:220px"><label>Address*</label><div>Enter your address</div></div>
  <div class="field" style="left:520px;top:3490px;width:470px"><label>Message*</label><div style="height:110px">Type your text here</div></div>
  <div class="send">Send</div>
</section>

<section class="banner">
  <div class="photo" role="img" aria-label="Photo of a bronze statue of Lady Justice holding scales" style="left:0;top:0;width:560px;height:432px;background:linear-gradient(90deg,#ffffff,#e7e4de 40%,#a88f6a 75%,#f2f0ec)"></div>
  <div class="banner-text">
    <h2>Kellow<br>Family Law</h2>
    <p>Collaborative law and unbundled legal services in King County, Washington state...</p>
    <span class="btn">Contact Me</span>
  </div>
</section>

<footer class="site-footer">
  <h2 class="section-title">Newsletter</h2>
  <div class="newsletter">Enter your email address<span class="go"></span></div>
  <div class="foot-brand"><div class="brand-mark" style="width:64px;height:64px"></div><div class="brand-name" style="font-size:24px">Kellow<br>Family Law</div></div>
  <div class="socials"><span></span><span></span><span></span><span></span></div>
  <div class="foot-col" style="left:430px"><h5>Quick Links</h5><a>About</a><a>Collaborative law</a><a>Cost &amp; fees</a><a>Mediation</a><a>Trusting in the Collaborative</a><a>Blog &amp; Articles</a></div>
  <div class="foot-col" style="left:680px"><h5>Information</h5><a>Site Map</a><a>Terms &amp; Condition</a><a>Privacy Policy</a><a>FAQ's</a><a>Customer Service</a><a>Disclaimer</a></div>
  <div class="foot-col" style="left:900px"><h5>Contact Us</h5><a>Email:<br>www.kellowlaw.test</a><a>Phone:<br>(+00) 321 654 09</a><a>Location:<br>Some address line goes here city name</a></div>
  <div class="copyright">© 2022. Kellow Family Law. All rights reserved</div>
</footer>

</body>
</html>
```